Design a WordPress layout for a home loans company

The home loans company in question is going through a rebrand and needs a new website layout.
Sites they like: http://www.brightnestlending.com.au/
Current logo: Attached.
Colours to be used: As per those used in logo.
Primary: #71aa3d
Secondary: #130e10
Pages to be designed:
- Homepage
- Internal services page
Menu items for display purposes:
- Home
- About Us
- Speak to a Broker
- Articles
- Contact Us
A modern design with simplicity is key.
For copy, dummy text such as Lorem ipsum will be fine.
If you would like anything elso, please ask.
Target Market(s)
25-40 year old
Mostly female
Buying their first home in most cases
Industry/Entity Type
Mortgage Brokerage
Number of Pages Required
2 page
Colors
Designer to choose colors to be used in the design.
Look and feel

```html
<!DOCTYPE html>
<html lang="en">
<head>
<meta charset="utf-8">
<title>Harbourline Home Loans</title>
<link rel="stylesheet" href="https://fonts.googleapis.com/css2?family=Open+Sans:wght@400;600;700&family=Raleway:wght@600;700;800&display=swap">
<style>
:root{
  --green:#71aa3d;
  --green-dark:#5f9530;
  --ink:#130e10;
  --text:#222;
  --muted:#7a7a7a;
  --line:#dcdcdc;
  --grey-band:#f0f0f0;
  --white:#fff;
}
*{box-sizing:border-box;margin:0;padding:0}
html,body{width:1200px;height:3468px;overflow:hidden}
body{font-family:"Open Sans",Arial,sans-serif;color:var(--text);background:var(--white);position:relative}
.abs{position:absolute}
.head-font{font-family:"Raleway","Open Sans",sans-serif}

/* header */
.site-header{position:absolute;left:0;top:0;width:1200px;height:102px;background:var(--white)}
.brand{position:absolute;left:97px;top:20px;display:flex;align-items:center;gap:12px;font-family:"Raleway",sans-serif;font-weight:800;font-size:30px;color:var(--green);line-height:1}
.brand-mark{width:22px;height:22px;background:var(--green)}
.top-contact{position:absolute;right:97px;top:22px;font-size:16px;font-weight:600;color:var(--ink);display:flex;align-items:center;gap:10px}
.top-contact svg{fill:var(--green)}
.main-nav{position:absolute;right:86px;top:62px;display:flex;gap:40px;font-family:"Raleway",sans-serif;font-weight:700;font-size:16px;color:var(--ink);text-transform:uppercase;align-items:center}
.main-nav .active{color:var(--green)}

/* hero */
.hero{position:absolute;left:0;top:102px;width:1200px;height:570px;background:linear-gradient(100deg,#6f5a4a 0%,#a8876c 35%,#cdb59b 60%,#8c7360 100%);overflow:hidden}
.hero-title{position:absolute;left:97px;top:128px;font-family:"Raleway",sans-serif;font-weight:800;font-size:60px;color:var(--white);letter-spacing:1px}
.hero-sub{position:absolute;left:97px;top:210px;font-size:26px;color:var(--white)}
.search{position:absolute;left:97px;top:284px;width:546px;height:51px;display:flex}
.search-field{flex:1;background:var(--white);display:flex;align-items:center;gap:10px;padding-left:22px;font-size:15px;color:#555}
.search-btn{width:151px;background:var(--green);color:var(--white);font-weight:700;font-size:17px;display:flex;align-items:center;justify-content:center}
.dots{position:absolute;left:565px;top:407px;display:flex;gap:5px}
.dots span{width:12px;height:12px;border-radius:50%;border:2px solid var(--white)}
.dots span:first-child{background:var(--white)}
.hero-curve{position:absolute;left:0;bottom:0}

/* section titles */
.section-title{position:absolute;left:0;width:1200px;text-align:center;font-family:"Raleway",sans-serif;font-weight:700;font-size:36px;color:var(--ink)}
.section-intro{position:absolute;left:200px;width:800px;text-align:center;font-size:15px;line-height:29px;color:var(--muted)}

/* feature cards */
.feature{position:absolute;top:844px;width:234px;height:250px;border:1px solid var(--line);text-align:center}
.feature-icon{width:100px;height:100px;border-radius:50%;background:var(--green);margin:26px auto 0;display:flex;align-items:center;justify-content:center}
.feature h3{font-family:"Raleway",sans-serif;font-weight:700;font-size:21px;color:var(--ink);margin-top:22px}
.feature p{font-size:13px;line-height:22px;color:var(--muted);margin:8px 20px 0}

/* what we do */
.what-band{position:absolute;left:0;top:1184px;width:1200px;height:534px;background:linear-gradient(90deg,#6d6a62 0%,#8d857a 40%,#a4978b 70%,#6e5a4c 100%)}
.what-card{position:absolute;left:97px;top:1260px;width:1003px;height:379px;background:rgba(255,255,255,.95)}
.what-media{position:absolute;left:0;top:0;width:467px;height:379px;background:linear-gradient(135deg,#d8d3c8,#9c8f7e 60%,#6a5c4e)}
.play{position:absolute;left:196px;top:152px}
.what-body{position:absolute;left:504px;top:46px;width:470px}
.what-body h2{font-family:"Raleway",sans-serif;font-weight:700;font-size:34px;color:var(--ink)}
.what-body p{font-size:14px;line-height:25px;color:#555;margin-top:20px}
.btn-solid{display:inline-flex;align-items:center;justify-content:center;background:var(--green);color:var(--white);font-weight:700;font-size:14px;border-radius:22px;text-transform:uppercase}
.what-body .btn-solid{width:128px;height:42px;margin-top:22px}

/* compare */
.option{position:absolute;top:1963px;width:324px;height:277px;display:flex;align-items:flex-end;justify-content:center;padding-bottom:30px}
.option span{font-family:"Raleway",sans-serif;font-weight:700;font-size:24px;color:var(--white)}
.opt-1{left:97px;background:linear-gradient(160deg,#7a4b2e,#a6713f 50%,#3c2c24)}
.opt-2{left:438px;background:linear-gradient(160deg,#a59d90,#6b6258 60%,#3b342e)}
.opt-3{left:779px;background:linear-gradient(160deg,#e2e0dd,#aab3b8 55%,#5c6870)}
.slide-arrow{position:absolute;top:2081px;width:40px;height:40px;border-radius:50%;border:2px solid #444;display:flex;align-items:center;justify-content:center}
.btn-outline{position:absolute;display:flex;align-items:center;justify-content:center;border:2px solid var(--green);color:var(--green);font-weight:700;font-size:16px;border-radius:32px;text-transform:uppercase;background:var(--white)}

/* blog */
.blog-band{position:absolute;left:0;top:2474px;width:1200px;height:560px;background:var(--grey-band)}
.post-thumb{position:absolute;top:2647px;width:218px;height:185px;border:4px solid var(--white)}
.post{position:absolute;top:2645px;width:250px}
.post h3{font-family:"Raleway",sans-serif;font-weight:700;font-size:19px;line-height:28px;color:var(--ink)}
.post .meta{font-size:12px;color:#555;margin-top:10px;display:flex;align-items:center;gap:8px}
.post p{font-size:13px;line-height:21px;color:#666;margin-top:14px}
.post .more{font-size:13px;font-weight:700;color:var(--green);margin-top:14px;text-transform:uppercase}

/* footer */
.site-footer{position:absolute;left:0;top:2980px;width:1200px;height:488px}
.footer-brand{position:absolute;left:97px;top:3228px;display:flex;align-items:center;gap:12px;font-family:"Raleway",sans-serif;font-weight:800;font-size:30px;color:var(--white)}
.footer-brand .brand-mark{background:var(--white)}
.footer-col{position:absolute;top:3160px;color:var(--white)}
.footer-col h4{font-family:"Raleway",sans-serif;font-weight:700;font-size:17px;text-transform:uppercase;letter-spacing:.3px}
.quick-links{list-style:none;margin-top:20px;font-size:12.5px;line-height:26.5px}
.news p{font-size:12.5px;line-height:22px;margin-top:22px;width:240px}
.news-input{width:252px;height:32px;background:var(--white);color:#555;font-size:12px;padding-left:10px;display:flex;align-items:center;margin-top:14px}
.news .btn-solid{width:100px;height:30px;font-size:12px;margin-top:16px}
.contact-line{display:flex;align-items:flex-start;gap:14px;font-size:12.5px;line-height:20px;margin-top:22px}
.contact-line svg{fill:var(--white);flex:none;margin-top:2px}
.footer-rule{position:absolute;left:97px;top:3390px;width:1006px;height:1px;background:#3a3537}
.copyright{position:absolute;left:97px;top:3417px;font-size:12px;color:var(--white)}
.social{position:absolute;left:973px;top:3413px;display:flex;gap:8px}
.social span{width:26px;height:26px;border-radius:50%;border:1.5px solid var(--white)}
</style>
</head>
<body>

<header class="site-header">
  <div class="brand"><span class="brand-mark"></span>Harbourline Home Loans</div>
  <div class="top-contact">
    <svg width="16" height="16" viewBox="0 0 24 24"><path d="M6.6 10.8c1.4 2.8 3.8 5.1 6.6 6.6l2.2-2.2c.3-.3.7-.4 1-.2 1.1.4 2.3.6 3.6.6.6 0 1 .4 1 1V20c0 .6-.4 1-1 1C10.6 21 3 13.4 3 4c0-.6.4-1 1-1h3.5c.6 0 1 .4 1 1 0 1.3.2 2.5.6 3.6.1.3 0 .7-.2 1z"/></svg>
    (08) 5550 0142 &nbsp;|&nbsp;
    <svg width="18" height="14" viewBox="0 0 24 18"><path d="M0 0h24v2L12 10 0 2z M0 4.5l12 8 12-8V18H0z"/></svg>
    info@harbourlinehomeloans.com
  </div>
  <nav class="main-nav">
    <span class="active">Home</span><span>About Us</span><span>Speak to Broker</span><span>Articles</span><span>Contact Us</span>
    <svg width="16" height="16" viewBox="0 0 24 24"><circle cx="10" cy="10" r="7" fill="none" stroke="#130e10" stroke-width="3"/><path d="M15 15l7 7" stroke="#130e10" stroke-width="3"/></svg>
  </nav>
</header>

<section class="hero" role="img" aria-label="Family of four laughing together on a living room sofa">
  <h1 class="hero-title">HARBOURLINE HOME LOANS</h1>
  <p class="hero-sub">At vero eos et accusamus et iusto oigni</p>
  <div class="search">
    <div class="search-field">
      <svg width="12" height="16" viewBox="0 0 12 16"><path d="M6 0a6 6 0 0 1 6 6c0 4.5-6 10-6 10S0 10.5 0 6a6 6 0 0 1 6-6zm0 3.5a2.5 2.5 0 1 0 0 5 2.5 2.5 0 0 0 0-5z" fill="#333"/></svg>
      Enter a Location or PostCode
    </div>
    <div class="search-btn">FIND BROKER</div>
  </div>
  <div class="dots"><span></span><span></span><span></span><span></span></div>
  <svg class="hero-curve" width="1200" height="110" viewBox="0 0 1200 110">
    <path d="M0 110 L0 60 Q600 -30 1200 60 L1200 110 Z" fill="#fff"/>
    <path d="M0 60 Q600 -30 1200 60" fill="none" stroke="#71aa3d" stroke-width="7"/>
  </svg>
</section>

<h2 class="section-title" style="top:683px">WELCOME TO HARBOURLINE HOME LOANS</h2>
<p class="section-intro" style="top:744px">At vero eos et accusamus et iusto odio dignissimos ducimus qui blanditiis praesentium voluptatum deleniti atque corrupti quos dolores et quas molestias excepturi sint occaecati cupiditate non provident, similique sunt in culp</p>

<div class="feature" style="left:97px">
  <div class="feature-icon"><svg width="44" height="44" viewBox="0 0 24 24" fill="#fff"><circle cx="12" cy="8" r="4.5"/><path d="M3 21c0-5 4-8 9-8s9 3 9 8z"/></svg></div>
  <h3>Local experts</h3>
  <p>Nemo enim ipsam voluptatequ ia volu ptas sit asperna</p>
</div>
<div class="feature" style="left:354px">
  <div class="feature-icon"><svg width="48" height="44" viewBox="0 0 26 24" fill="none" stroke="#fff" stroke-width="2"><ellipse cx="14" cy="10" rx="10" ry="7.5"/><path d="M7 16l-4 5 7-2.5"/><path d="M9 10h10M9 13h6"/></svg></div>
  <h3>Trusted advice</h3>
  <p>Nemo enim ipsam voluptatequ ia volu ptas sit asperna</p>
</div>
<div class="feature" style="left:611px">
  <div class="feature-icon"><svg width="44" height="44" viewBox="0 0 24 24"><circle cx="10" cy="10" r="6.5" fill="none" stroke="#fff" stroke-width="3"/><path d="M15 15l6.5 6.5" stroke="#fff" stroke-width="3.5" stroke-linecap="round"/></svg></div>
  <h3>Find a broker</h3>
  <p>Nemo enim ipsam voluptatequ ia volu ptas sit asperna</p>
</div>
<div class="feature" style="left:868px">
  <div class="feature-icon"><svg width="40" height="46" viewBox="0 0 20 24" fill="#fff"><path d="M2 0h16a2 2 0 0 1 2 2v20a2 2 0 0 1-2 2H2a2 2 0 0 1-2-2V2a2 2 0 0 1 2-2zm1 3v5h14V3zm0 8v3h3v-3zm5.5 0v3h3v-3zm5.5 0v3h3v-3zM3 16v3h3v-3zm5.5 0v3h3v-3zm5.5 0v3h3v-3z" fill-rule="evenodd"/></svg></div>
  <h3>Calculators &amp; tools</h3>
  <p>Nemo enim ipsam voluptatequ ia volu ptas sit asperna</p>
</div>

<div class="what-band" role="img" aria-label="Blurred background of a couple meeting with a broker"></div>
<div class="what-card">
  <div class="what-media" role="img" aria-label="Video still of a family reviewing loan papers with an advisor">
    <svg class="play" width="76" height="76" viewBox="0 0 76 76"><circle cx="38" cy="38" r="36" fill="#130e10" opacity=".85" stroke="#fff" stroke-width="2"/><path d="M30 24l24 14-24 14z" fill="#fff"/></svg>
  </div>
  <div class="what-body">
    <h2>WHAT WE DO</h2>
    <p>Nam libero tempore, cum soluta nobis est eligendi optio cumque nihil imp edit quo minus id quod maxime placeat facere possi.</p>
    <p>Monis voluptas assumenda est, omnis dolor repellendus. Temporibus aut emqu ibusdam et aut officiis debitis aut rerum necessitatibus saepe eveni et ut volo ptates repudiandae sint et molestiae non recusandae. Itaque earum rerum hic tenetur a sapiente delec.</p>
    <span class="btn-solid">Read More</span>
  </div>
</div>

<h2 class="section-title" style="top:1804px">COMPARE HOME LOAN OPTIONS</h2>
<p class="section-intro" style="top:1866px">At vero eos et accusamus et iusto odio dignissimos ducimus qui blanditiis praesentium voluptatum deleniti atque corrupti quos dolores et quas molestias excepturi sint occaecati cupiditate non provident, similique sunt in culp</p>

<div class="slide-arrow" style="left:26px"><svg width="12" height="14" viewBox="0 0 12 14"><path d="M9 1L3 7l6 6" fill="none" stroke="#333" stroke-width="2.5"/></svg></div>
<div class="option opt-1" role="img" aria-label="Couple discussing refinancing with an advisor"><span>Refinancing a loan</span></div>
<div class="option opt-2" role="img" aria-label="Couple framed by a house outline, property investment"><span>Investing in Property</span></div>
<div class="option opt-3" role="img" aria-label="Smiling couple buying their first home"><span>Buying Your First Home</span></div>
<div class="slide-arrow" style="left:1127px"><svg width="12" height="14" viewBox="0 0 12 14"><path d="M3 1l6 6-6 6" fill="none" stroke="#333" stroke-width="2.5"/></svg></div>

<div class="btn-outline" style="left:416px;top:2303px;width:366px;height:62px">Compare your home loan options</div>

<div class="blog-band"></div>
<h2 class="section-title" style="top:2551px">RECENT BLOG</h2>

<div class="post-thumb" style="left:97px;background:linear-gradient(135deg,#e8c48a,#c2492f 50%,#3d7fc0)" role="img" aria-label="Couple holding a small model house"></div>
<div class="post" style="left:342px">
  <h3>Nemo enim ipsam voluptat em quia voluptsit</h3>
  <div class="meta">
    <svg width="12" height="12" viewBox="0 0 12 12"><rect x="0" y="1.5" width="12" height="10.5" fill="#71aa3d"/><rect x="1.5" y="4.5" width="9" height="6" fill="#fff"/></svg>17/08/2017 &nbsp;|&nbsp;
    <svg width="11" height="12" viewBox="0 0 11 12" fill="#71aa3d"><circle cx="5.5" cy="3" r="3"/><path d="M0 12c0-4 2.5-5.5 5.5-5.5S11 8 11 12z"/></svg>John Doe
  </div>
  <p>Ut enim ad minima veniam, quis nos trum exercitationem ullam corporisu scipit laboriosam, nisi.</p>
  <div class="more">Read More</div>
</div>

<div class="post-thumb" style="left:615px;background:linear-gradient(135deg,#dfe7ee,#9fb2c4 55%,#6c7b86)" role="img" aria-label="Model house on loan documents"></div>
<div class="post" style="left:865px">
  <h3>Nemo enim ipsam voluptat em quia voluptsit</h3>
  <div class="meta">
    <svg width="12" height="12" viewBox="0 0 12 12"><rect x="0" y="1.5" width="12" height="10.5" fill="#71aa3d"/><rect x="1.5" y="4.5" width="9" height="6" fill="#fff"/></svg>17/08/2017 &nbsp;|&nbsp;
    <svg width="11" height="12" viewBox="0 0 11 12" fill="#71aa3d"><circle cx="5.5" cy="3" r="3"/><path d="M0 12c0-4 2.5-5.5 5.5-5.5S11 8 11 12z"/></svg>John Doe
  </div>
  <p>Ut enim ad minima veniam, quis nos trum exercitationem ullam corporisu scipit laboriosam, nisi.</p>
  <div class="more">Read More</div>
</div>

<div class="btn-outline" style="left:506px;top:2906px;width:188px;height:63px;background:transparent">View All Post</div>

<footer class="site-footer">
  <svg class="abs" style="left:0;top:0" width="1200" height="488" viewBox="0 0 1200 488">
    <path d="M0 8 Q600 130 1200 8 L1200 488 L0 488 Z" fill="#130e10"/>
    <path d="M0 8 Q600 130 1200 8" fill="none" stroke="#71aa3d" stroke-width="5"/>
  </svg>
</footer>

<div class="footer-brand"><span class="brand-mark"></span>Harbourline<br>Home Loans</div>

<div class="footer-col" style="left:414px">
  <h4>Quick Links</h4>
  <ul class="quick-links">
    <li>Customer Log In</li><li>About Us</li><li>How it Works</li><li>FAQ's</li><li>Blog</li><li>Contact Us</li>
  </ul>
</div>

<div class="footer-col news" style="left:592px">
  <h4>Newsletter Subscription</h4>
  <p>Register your Email Address to get Information about us</p>
  <div class="news-input">Email Address</div>
  <span class="btn-solid">Subscribe</span>
</div>

<div class="footer-col" style="left:927px">
  <h4>Contact Us</h4>
  <div class="contact-line"><svg width="11" height="15" viewBox="0 0 12 16"><path d="M6 0a6 6 0 0 1 6 6c0 4.5-6 10-6 10S0 10.5 0 6a6 6 0 0 1 6-6zm0 3.5a2.5 2.5 0 1 0 0 5 2.5 2.5 0 0 0 0-5z"/></svg><span>27 Larkspur Rd Northbridge,<br>Western Australia</span></div>
  <div class="contact-line"><svg width="14" height="14" viewBox="0 0 24 24"><path d="M6.6 10.8c1.4 2.8 3.8 5.1 6.6 6.6l2.2-2.2c.3-.3.7-.4 1-.2 1.1.4 2.3.6 3.6.6.6 0 1 .4 1 1V20c0 .6-.4 1-1 1C10.6 21 3 13.4 3 4c0-.6.4-1 1-1h3.5c.6 0 1 .4 1 1 0 1.3.2 2.5.6 3.6.1.3 0 .7-.2 1z"/></svg><span>(08) 5550 0142</span></div>
  <div class="contact-line"><svg width="15" height="12" viewBox="0 0 24 18"><path d="M0 0h24v2L12 10 0 2z M0 4.5l12 8 12-8V18H0z"/></svg><span>info@harbourlinehomeloans.com</span></div>
</div>

<div class="footer-rule"></div>
<p class="copyright">Copyrights © 2018, Harbourline home loans. &nbsp;All rights reserved.</p>
<div class="social" aria-label="Social links"><span></span><span></span><span></span><span></span></div>

</body>
</html>
```